Kestrel Builders Business Card Design Project

Clean sharp business card
Ability to write on back of card
Details for the card -
Address: PO Box 5867, Marrowdale, Qld, 4291
ABN: 47 305 961 220
BSA LIC 2650874
Ph: 07 3562 4470
Fax: 07 3562 4475
Email: kestrelbuilders@mailbrook.com.au

```html
<!DOCTYPE html>
<html lang="en">
<head>
<meta charset="utf-8">
<title>Kestrel Builders – Business Cards</title>
<link href="https://fonts.googleapis.com/css2?family=Arimo:wght@400;700&display=swap" rel="stylesheet">
<style>
  :root {
    --backdrop: #7a4424;
    --card: #262324;
    --name: #e8562a;
    --text: #f2f2f2;
    --icon: #e8562a;
    --gold: #c99732;
    --silver: #d9d9d9;
  }
  * { margin: 0; padding: 0; box-sizing: border-box; }
  html, body {
    width: 1200px; height: 900px; overflow: hidden;
    background: var(--backdrop);
    font-family: "Arimo", Arial, sans-serif;
  }
  .stage { position: relative; width: 1200px; height: 900px; }

  .card {
    position: absolute;
    background: var(--card);
    border-radius: 28px;
    overflow: hidden;
    color: var(--text);
    box-shadow: 0 6px 18px rgba(0,0,0,.35);
  }
  .card--front { left: 67px; top: 77px; width: 506px; height: 417px; }
  .card--back  { left: 584px; top: 411px; width: 556px; height: 418px; }

  .brand {
    position: absolute;
    font-weight: 700;
    font-size: 26px;
    letter-spacing: .5px;
    color: var(--text);
    white-space: nowrap;
    transform: translateX(-50%);
  }
  .card--front .brand { left: 253px; top: 76px; }
  .card--back .brand  { left: 276px; top: 78px; }

  .person {
    position: absolute;
    color: var(--name);
    font-size: 25px;
    font-weight: 400;
  }
  .card--front .person { left: 41px; top: 146px; }
  .card--back .person  { left: 39px; top: 146px; }

  .details {
    position: absolute;
    font-size: 15.5px;
    line-height: 22.5px;
    white-space: nowrap;
  }
  .details--email { font-size: 12px; }

  .card--front .details--postal { left: 39px; top: 204px; }
  .card--front .details--contact { left: 288px; top: 207px; }

  .card--back .details--postal { left: 59px; top: 204px; }
  .card--back .details--contact { left: 306px; top: 206px; }

  .row { display: flex; align-items: center; gap: 7px; }
  .row svg { width: 12px; height: 12px; flex: none; }

  .divider {
    position: absolute;
    width: 2px;
    height: 82px;
    background: linear-gradient(to bottom, transparent, var(--silver) 50%, transparent);
  }
  .card--front .divider { left: 246px; top: 208px; }
  .card--back .divider  { left: 268px; top: 210px; }

  .rule {
    position: absolute; left: 0; right: 0; height: 4px;
    background: linear-gradient(to right, #3a3a3a, var(--silver) 35%, #ffffff 50%, var(--silver) 65%, #3a3a3a);
  }
  .band {
    position: absolute; left: 0; right: 0; height: 45px;
    background: var(--gold);
  }
  .card--front .rule { top: 322px; }
  .card--front .band { top: 335px; }
  .card--back .rule { top: 324px; }
  .card--back .band { top: 336px; }
</style>
</head>
<body>
<div class="stage">

  <section class="card card--front">
    <div class="brand">Kestrel Builders</div>
    <div class="person">YOUR NAME</div>
    <div class="details details--postal">
      <div>Address : PO Box 5867,</div>
      <div>Marrowdale, Qld, 4291</div>
      <div>ABN :&nbsp; 47 305 961 220</div>
      <div>BAS LIC 2650874</div>
    </div>
    <div class="divider"></div>
    <div class="details details--contact">
      <div>Tel : 35624470</div>
      <div>Fax : 35624475</div>
      <div class="details--email">E : kestrelbuilders@mailbrook.com.au</div>
    </div>
    <div class="rule"></div>
    <div class="band"></div>
  </section>

  <section class="card card--back">
    <div class="brand">Kestrel Builders</div>
    <div class="person">YOUR NAME</div>
    <div class="details details--postal">
      <div class="row" style="margin-left:-20px">
        <svg viewBox="0 0 12 12" aria-hidden="true"><path d="M6 1 L11 6 H9.5 V11 H7 V8 H5 V11 H2.5 V6 H1 Z" fill="none" stroke="var(--icon)" stroke-width="1.4"/></svg>
        <span>PO Box 5867,</span>
      </div>
      <div>Marrowdale, Qld, 4291</div>
      <div>ABN :&nbsp; 47 305 961 220</div>
      <div>BAS LIC 2650874</div>
    </div>
    <div class="divider"></div>
    <div class="details details--contact">
      <div class="row">
        <svg viewBox="0 0 12 12" aria-hidden="true"><path d="M2.5 1 L4.5 1 L5.2 3.5 L3.9 4.5 C4.6 6 6 7.4 7.5 8.1 L8.5 6.8 L11 7.5 L11 9.5 C11 10.4 10.3 11 9.5 11 C5 10.6 1.4 7 1 2.5 C1 1.7 1.6 1 2.5 1 Z" fill="var(--icon)"/></svg>
        <span>35624470</span>
      </div>
      <div class="row">
        <svg viewBox="0 0 12 12" aria-hidden="true"><rect x="3" y="1" width="6" height="3" fill="none" stroke="var(--icon)" stroke-width="1.2"/><rect x="1" y="4.5" width="10" height="4.5" fill="var(--icon)"/><rect x="3" y="8" width="6" height="3" fill="none" stroke="var(--icon)" stroke-width="1.2"/></svg>
        <span>35624475</span>
      </div>
      <div class="row details--email">
        <svg viewBox="0 0 12 12" aria-hidden="true"><rect x="0.5" y="2.5" width="11" height="7" fill="var(--icon)"/><path d="M0.5 2.5 L6 6.5 L11.5 2.5" fill="none" stroke="var(--card)" stroke-width="1"/></svg>
        <span>kestrelbuilders@mailbrook.com.au</span>
      </div>
    </div>
    <div class="rule"></div>
    <div class="band"></div>
  </section>

</div>
</body>
</html>
```